MVDP

Need a 3:2 ratio image for a billboard. We'd like this image (free Brantle image) or another showing the chaos of the January 6th attack on the Morwick Hall. Across the bottom it needs to read "POLITICAL AD PAID FOR BY THE MARLOW VALE DEMOCRATIC PARTY AND TESSALY RIDGE DEMOCRATS"

```html
<!DOCTYPE html>
<html lang="en">
<head>
<meta charset="utf-8">
<title>Had Enough? — MVDP Billboard</title>
<link href="https://fonts.googleapis.com/css2?family=Oswald:wght@600;700&display=swap" rel="stylesheet">
<style>
  :root {
    --page-bg: #e9ecef;
    --sky-light: #c3c6cb;
    --sky-grey: #8d949d;
    --storm-dark: #17191d;
    --crowd-dark: #1e1d24;
    --flag-red: #b02e3a;
    --flag-blue: #2f4596;
    --stone: #e4e1da;
    --band-yellow: #e2ef00;
    --ink: #0d0d0d;
    --white: #ffffff;
  }
  * { margin: 0; padding: 0; box-sizing: border-box; }
  html, body { width: 1200px; height: 840px; overflow: hidden; background: var(--page-bg); }
  .billboard {
    position: absolute; left: 0; top: 20px;
    width: 1200px; height: 800px; overflow: hidden;
    background: var(--crowd-dark);
  }
  .scene-photo { position: absolute; left: 0; top: 0; width: 1200px; height: 680px; }
  .headline {
    position: absolute; right: 92px; top: 70px;
    font-family: 'Oswald', sans-serif; font-weight: 700;
    color: var(--white); text-align: center;
    font-size: 168px; line-height: 0.98; letter-spacing: 1px;
    text-shadow: 3px 5px 10px rgba(0,0,0,0.5);
  }
  .disclaimer-band { position: absolute; left: 0; bottom: 0; width: 1200px; height: 250px; }
  .disclaimer {
    position: absolute; left: 0; right: 0; bottom: 52px;
    font-family: 'Oswald', sans-serif; font-weight: 600;
    color: var(--ink); text-align: center;
    font-size: 44px; line-height: 1.08;
  }
</style>
</head>
<body>
  <main class="billboard">
    <svg class="scene-photo" viewBox="0 0 1200 680" preserveAspectRatio="none" role="img" aria-label="Photograph of a crowd with flags storming the steps and scaffolding of the Morwick Hall under a stormy sky">
      <defs>
        <linearGradient id="sky" x1="0" y1="0" x2="1" y2="0.6">
          <stop offset="0" stop-color="var(--sky-light)"/>
          <stop offset="0.45" stop-color="var(--sky-grey)"/>
          <stop offset="1" stop-color="var(--storm-dark)"/>
        </linearGradient>
        <radialGradient id="hall" cx="0.22" cy="0.55" r="0.32">
          <stop offset="0" stop-color="var(--stone)"/>
          <stop offset="1" stop-color="var(--stone)" stop-opacity="0"/>
        </radialGradient>
        <linearGradient id="crowd" x1="0" y1="0" x2="0" y2="1">
          <stop offset="0" stop-color="var(--crowd-dark)" stop-opacity="0"/>
          <stop offset="0.45" stop-color="var(--crowd-dark)" stop-opacity="0.85"/>
          <stop offset="1" stop-color="var(--crowd-dark)"/>
        </linearGradient>
        <radialGradient id="redFlags" cx="0.5" cy="0.5" r="0.5">
          <stop offset="0" stop-color="var(--flag-red)" stop-opacity="0.75"/>
          <stop offset="1" stop-color="var(--flag-red)" stop-opacity="0"/>
        </radialGradient>
        <radialGradient id="blueFlag" cx="0.5" cy="0.5" r="0.5">
          <stop offset="0" stop-color="var(--flag-blue)" stop-opacity="0.85"/>
          <stop offset="1" stop-color="var(--flag-blue)" stop-opacity="0"/>
        </radialGradient>
      </defs>
      <rect width="1200" height="680" fill="url(#sky)"/>
      <rect width="1200" height="680" fill="url(#hall)"/>
      <rect y="380" width="1200" height="300" fill="url(#crowd)"/>
      <ellipse cx="330" cy="560" rx="320" ry="90" fill="url(#redFlags)"/>
      <ellipse cx="900" cy="560" rx="330" ry="90" fill="url(#blueFlag)"/>
      <ellipse cx="760" cy="600" rx="200" ry="60" fill="url(#redFlags)"/>
    </svg>
    <h1 class="headline">HAD<br>ENOUGH?</h1>
    <svg class="disclaimer-band" viewBox="0 0 1200 250" preserveAspectRatio="none" aria-hidden="true">
      <path d="M0 60 C 420 55, 860 35, 1200 0 L1200 250 L0 250 Z" fill="var(--band-yellow)"/>
    </svg>
    <p class="disclaimer">POLITICAL AD PAID FOR BY THE MARLOW VALE DEMOCRATIC PARTY<br>AND TESSALY RIDGE DEMOCRATS</p>
  </main>
</body>
</html>
```